Marrowfield Contracting Business Cards

Front of card:

Full Logo
Name
Address
Office Phone
Cell Phone
Email
Website

Back:
Logo Mark in background
List and markets and services performed

```html
<!DOCTYPE html>
<html lang="en">
<head>
<meta charset="utf-8">
<title>Marrowfield Contracting Business Cards</title>
<link rel="stylesheet" href="https://fonts.googleapis.com/css2?family=Jost:wght@400;500;600;700&display=swap">
<style>
  :root {
    --backdrop: #2e2f31;
    --brand-red: #d41f26;
    --brand-red-deep: #b8151c;
    --ink-grey: #555659;
    --rule-grey: #b9babc;
    --card-white: #ffffff;
    --card-mist: #e9e9ea;
  }
  * { box-sizing: border-box; margin: 0; padding: 0; }
  html, body {
    width: 1200px; height: 900px; overflow: hidden;
    background: var(--backdrop);
    font-family: "Jost", "Futura", sans-serif;
  }
  .sheet {
    position: relative; width: 1200px; height: 900px;
    display: flex; flex-direction: column; align-items: center;
    justify-content: center; gap: 40px;
  }
  .card {
    position: relative; width: 700px; height: 400px;
    border-radius: 30px; overflow: hidden;
    box-shadow: 0 14px 30px rgba(0,0,0,.45);
  }

  /* Back side */
  .card-back { background: var(--brand-red); color: var(--card-white); }
  .card-back .pattern-field {
    position: absolute; inset: 0;
    background: radial-gradient(ellipse at 30% 30%, #dc252c 0%, var(--brand-red) 55%, var(--brand-red-deep) 100%);
  }
  .back-content {
    position: relative; height: 100%;
    display: flex; flex-direction: column; align-items: center; justify-content: center;
    text-align: center; gap: 16px;
  }
  .info-block h2 { font-size: 20px; font-weight: 700; line-height: 1.2; }
  .info-block li { list-style: none; font-size: 17px; font-weight: 400; line-height: 1.15; }
  .info-block p { font-size: 17px; line-height: 1.2; max-width: 520px; }

  /* Front side */
  .card-front {
    background: linear-gradient(160deg, var(--card-white) 0%, #f6f6f6 45%, var(--card-mist) 100%);
    color: var(--ink-grey);
  }
  .holder {
    position: absolute; left: 40px; top: 150px;
  }
  .holder-line { display: flex; align-items: baseline; gap: 8px; font-size: 21px; }
  .holder-name { color: var(--brand-red); font-weight: 600; letter-spacing: .5px; }
  .holder-bar { color: var(--brand-red); font-weight: 600; }
  .holder-role { color: var(--ink-grey); }
  .holder-cell { display: flex; align-items: center; gap: 10px; margin-top: 4px; font-size: 20px; }
  .contact-list {
    position: absolute; right: 36px; top: 48px; list-style: none;
  }
  .contact-list li { display: flex; align-items: center; gap: 10px; font-size: 17px; line-height: 1.55; }
  .contact-list svg { flex: none; }
  .divider {
    position: absolute; right: 0; top: 188px; width: 390px; height: 1px; background: var(--rule-grey);
  }
  .brand-lockup {
    position: absolute; right: 40px; top: 235px;
    display: flex; align-items: center; gap: 14px;
  }
  .brand-dot { width: 26px; height: 26px; border-radius: 50%; background: var(--brand-red); }
  .brand-name { color: var(--brand-red); font-size: 30px; font-weight: 600; letter-spacing: .5px; }
</style>
</head>
<body>
<main class="sheet">

  <section class="card card-back" aria-label="Card back">
    <div class="pattern-field" role="img" aria-label="Repeating tone-on-tone brand pattern in red"></div>
    <div class="back-content">
      <div class="info-block">
        <h2>Services List</h2>
        <ul>
          <li>Concrete Structure</li>
          <li>Concrete Pavement</li>
          <li>Bridges</li>
          <li>Site Concrete</li>
        </ul>
      </div>
      <div class="info-block">
        <h2>Markets</h2>
        <ul>
          <li>Dummy Place 1</li>
          <li>Dummy Place 2</li>
          <li>Dummy Place 3</li>
          <li>Dummy Place 4</li>
        </ul>
      </div>
      <div class="info-block">
        <h2>Services Performed</h2>
        <p>Your Service details here Lorem Ipsum is simply dummy text of the printing and typesetting industry.</p>
      </div>
    </div>
  </section>

  <section class="card card-front" aria-label="Card front">
    <div class="holder">
      <div class="holder-line">
        <span class="holder-name">DANIEL REYES</span>
        <span class="holder-bar">|</span>
        <span class="holder-role">Director</span>
      </div>
      <div class="holder-cell">
        <svg width="12" height="20" viewBox="0 0 12 20" aria-hidden="true"><rect x="1" y="1" width="10" height="18" rx="2" fill="none" stroke="#d41f26" stroke-width="1.6"/><line x1="4" y1="16" x2="8" y2="16" stroke="#d41f26" stroke-width="1.4"/></svg>
        <span>555-014-2200</span>
      </div>
    </div>

    <ul class="contact-list">
      <li>
        <svg width="18" height="16" viewBox="0 0 18 16" aria-hidden="true"><path d="M1 5c0-3 16-3 16 0v2h-4V5H5v2H1z" fill="#d41f26"/><rect x="3" y="8" width="12" height="7" rx="1.5" fill="#d41f26"/></svg>
        <span>555-014-2200</span>
      </li>
      <li>
        <svg width="18" height="16" viewBox="0 0 18 16" aria-hidden="true"><rect x="1" y="3" width="16" height="11" rx="1.5" fill="#d41f26"/><path d="M1.5 4l7.5 6 7.5-6" fill="none" stroke="#fff" stroke-width="1.4"/></svg>
        <span>info@marrowfieldcontracting.com</span>
      </li>
      <li>
        <svg width="18" height="18" viewBox="0 0 18 18" aria-hidden="true"><circle cx="9" cy="9" r="7.5" fill="none" stroke="#d41f26" stroke-width="1.6"/><ellipse cx="9" cy="9" rx="3.2" ry="7.5" fill="none" stroke="#d41f26" stroke-width="1.3"/><line x1="1.5" y1="9" x2="16.5" y2="9" stroke="#d41f26" stroke-width="1.3"/></svg>
        <span>www.marrowfieldcontracting.com</span>
      </li>
      <li>
        <svg width="18" height="18" viewBox="0 0 18 18" aria-hidden="true"><path d="M9 1a6 6 0 0 1 6 6c0 4.5-6 10-6 10S3 11.5 3 7a6 6 0 0 1 6-6z" fill="#d41f26"/><circle cx="9" cy="7" r="2.2" fill="#fff"/></svg>
        <span>00 dummy city, dummy place 0000</span>
      </li>
    </ul>

    <div class="divider"></div>

    <div class="brand-lockup">
      <span class="brand-dot"></span>
      <span class="brand-name">MARROWFIELD CONTRACTING</span>
    </div>
  </section>

</main>
</body>
</html>
```